Bright Ridge Coatings

Hi
I'm looking for a unique and eye-catching design for my business card that reflects the identity of my business. We specialize in residential, commercial, insurance, real state, heritage,and body corporate painting services and I want the card to make a memorable impression on potential clients.

Key elements to include are:
- Our logo (attached)
- Contact information: my name is darian volkema but my short name is dar, im a director of this business, number: 0457893014, email: info@brightridgecoatings.com.au
Website: www.brightridgecoatings.com.au
Social media: facebook, instagram.

I'm open to creative ideas and unconventional formats, but it's important that the design maintains a professional look.

I'd like to see some initial concepts within the few days, and I'm willing to discuss any ideas you have.

Looking forward to seeing your creativity at work!

I prefer the colours pretty much the same as my logo, but i would be happy see if my logo match with other colours.
Thanks very much

Best regards,
Dar

Our target market consists of residential exterior and interior painting, basically we do all commercial jobs, bod corporate , heritage

Residential and commercial painting

All my information as provided!! Im not sure if you guys have access to my logo through with all the format in my account??

Serif

• My business card should be double sided,
• Its nice to have all my information in front and the rest at the back, like what we we do like residential , interior exterior and as i mentioned

```html
<!DOCTYPE html>
<html lang="en">
<head>
<meta charset="utf-8">
<title>Bright Ridge Coatings — Business Card</title>
<link rel="stylesheet" href="https://fonts.googleapis.com/css2?family=Arimo:wght@400;700&display=swap">
<style>
  :root {
    --bg-top: #d2d2d2;
    --bg-bottom: #a9a9a9;
    --card-white: #ffffff;
    --brand-blue: #2f5ea8;
    --brand-green: #246b2c;
    --brand-red: #c8191d;
    --text-grey: #555555;
    --text-dark: #333333;
  }
  * { box-sizing: border-box; margin: 0; padding: 0; }
  html, body { width: 1200px; height: 788px; overflow: hidden; }
  body {
    background: linear-gradient(180deg, var(--bg-top), var(--bg-bottom));
    font-family: "Arimo", Arial, sans-serif;
    position: relative;
  }
  .card {
    position: absolute;
    width: 540px;
    height: 310px;
    border-radius: 22px;
    overflow: hidden;
    box-shadow: 0 10px 24px rgba(0,0,0,0.28);
  }
  .card-front { left: 40px; top: 239px; background: var(--card-white); }
  .card-back { left: 620px; top: 239px; background: var(--brand-blue); }

  .edge-bands { position: absolute; inset: 0; width: 100%; height: 100%; }

  .brand-name {
    position: absolute;
    left: 40px; top: 44px;
    font-weight: 700;
    font-size: 25px;
    letter-spacing: 1.5px;
    text-transform: uppercase;
    color: var(--brand-blue);
  }
  .brand-rule {
    position: absolute;
    left: 40px; top: 82px;
    width: 330px; height: 2px;
    background: var(--brand-red);
  }
  .person { position: absolute; left: 74px; top: 112px; }
  .person-name {
    font-weight: 700;
    font-size: 24px;
    letter-spacing: 1px;
    text-transform: uppercase;
  }
  .person-name .first { color: var(--brand-green); }
  .person-name .last { color: var(--brand-blue); }
  .person-role { font-size: 15px; color: var(--text-grey); margin-top: 2px; }

  .contact-list {
    position: absolute;
    left: 74px; top: 182px;
    list-style: none;
  }
  .contact-list li {
    display: flex; align-items: center; gap: 8px;
    font-size: 14px; line-height: 22px;
    color: var(--text-dark);
  }
  .contact-icon { width: 12px; height: 12px; flex: none; }
  .social-dot {
    width: 11px; height: 11px; border-radius: 50%;
    background: var(--brand-blue); flex: none;
  }

  .back-brand {
    position: absolute;
    right: 36px; bottom: 60px;
    font-weight: 700;
    font-size: 27px;
    letter-spacing: 2px;
    text-transform: uppercase;
    color: var(--card-white);
  }
</style>
</head>
<body>

<section class="card card-front" aria-label="Business card front">
  <svg class="edge-bands" viewBox="0 0 540 310" preserveAspectRatio="none" aria-hidden="true">
    <rect class="band-green-block" x="0" y="262" width="28" height="48" fill="#246b2c"/>
    <polygon class="band-green" points="230,310 300,310 312,290 240,302" fill="#246b2c"/>
    <polygon class="band-blue" points="300,310 500,310 520,270 312,290" fill="#2f5ea8"/>
    <polygon class="band-red" points="500,310 540,310 540,230 520,270" fill="#c8191d"/>
  </svg>

  <div class="brand-name">Bright Ridge Coatings</div>
  <div class="brand-rule"></div>

  <div class="person">
    <div class="person-name"><span class="first">Darian</span> <span class="last">Volkema</span></div>
    <div class="person-role">Director</div>
  </div>

  <ul class="contact-list">
    <li>
      <svg class="contact-icon" viewBox="0 0 12 12" aria-hidden="true"><path d="M2 1h3l1 3-2 1a7 7 0 0 0 3 3l1-2 3 1v3a1 1 0 0 1-1 1A10 10 0 0 1 1 2a1 1 0 0 1 1-1z" fill="#2f5ea8"/></svg>
      0457893014
    </li>
    <li>
      <svg class="contact-icon" viewBox="0 0 12 12" aria-hidden="true"><rect x="0.5" y="2.5" width="11" height="7" fill="#2f5ea8"/><path d="M0.5 2.5l5.5 4 5.5-4" fill="none" stroke="#fff" stroke-width="1"/></svg>
      info@brightridgecoatings.com.au
    </li>
    <li>
      <svg class="contact-icon" viewBox="0 0 12 12" aria-hidden="true"><circle cx="6" cy="6" r="5.5" fill="#2f5ea8"/><path d="M0.5 6h11M6 0.5c-3 3-3 8 0 11M6 0.5c3 3 3 8 0 11" fill="none" stroke="#fff" stroke-width="0.8"/></svg>
      www.brightridgecoatings.com.au
    </li>
    <li>
      <span class="social-dot" aria-hidden="true"></span>
      brightridgecoatings
    </li>
  </ul>
</section>

<section class="card card-back" aria-label="Business card back">
  <div class="back-brand">Bright Ridge Coatings</div>
</section>

</body>
</html>
```